**Business Card**Designs Project** TorvaleHoldings,LLC

Im looking for a simple and elegant Business Card that has a professional Corporate look and feel. Im considering a Metal business card as well as 2 color layout, Embossed, 1 color two tone layout(File#6 like).

The card should NOT be too busy but subtle. Clean look providing Key Details.

please see uploaded files for actual logo and inspirational design i like.

See Uploaded File # 3 for Professional Logos Style

Target Market(s)

investors

Industry/Entity Type

Business

Contact Information for Business Card

Side 1 information
Torvale Holdings,LLC - Description Text below main logo = (Funding - Sales) or (Commercial - Residential) or (Property - Funding )
www.torvaleholdings.example

Side 2 Information =
Lem Korrin | Managing Broker
P 555-184-6072 | F 555-730-4158
E info@torvaleholdings.example
membership logos - see file #3 for stye and file #4 for inspiration

Side 2 = 10pt Font
BRE: 07261843
NMLS: 6827354

Colors
3277b5
5c5c5c
333333
959595
85acd3
1b1b1b
ffffff

Requirements
Must have
• Torvale Holdings, LLC **T Logo** - See Uploaded File #5 ,
• Contact Information - See Business Card Details Above
• Web address = www.torvaleholdings.example
• Membership logos - See Uploaded File #4 & 9
Nice to have
• 1 Color two tones, grey, White, Charcoal Grey, Dark Turquois, Dark blue, Slate blue,
• GOOD COMBINATIONS: White and Grey, white and Charcoal grey with a splash of blue, Charcoal grey card with White, etc..
• PLEASE TRY DARK BLUE DESIGNS
• Embossed, card designs
• Metal Business card design
Should not have
• I DONT LIKE ALOTE OF WAVE DESIGNS

```html
<!DOCTYPE html>
<html lang="en">
<head>
<meta charset="utf-8">
<title>Torvale Holdings, LLC — Business Cards</title>
<link rel="stylesheet" href="https://fonts.googleapis.com/css2?family=Questrial&family=Michroma&family=Roboto:wght@400&display=swap">
<style>
  :root {
    --backdrop: #1b1b1b;
    --card-dark: #232323;
    --card-dark-edge: #333333;
    --accent-blue: #3277b5;
    --accent-teal: #3a9dbf;
    --text-light: #d6d6d6;
    --text-mid: #959595;
    --text-dim: #5c5c5c;
    --metal-light: #d9d9d9;
    --metal-mid: #b4b4b4;
    --metal-dark: #8f8f8f;
    --metal-ink: #f4f4f4;
    --metal-line: #7a7a7a;
  }
  * { box-sizing: border-box; margin: 0; padding: 0; }
  html, body {
    width: 1200px; height: 871px; overflow: hidden;
    background: var(--backdrop);
  }
  .sheet { position: relative; width: 1200px; height: 871px; }

  .card {
    position: absolute; left: 250px; width: 700px; height: 400px;
    border-radius: 26px; overflow: hidden;
  }

  /* Back side — contact details */
  .card--back {
    top: 24px;
    background: linear-gradient(135deg, #2a2a2a, var(--card-dark) 60%, #1f1f1f);
    border: 1px solid var(--card-dark-edge);
  }
  .card--back .brand {
    position: absolute; left: 40px; top: 168px;
    display: flex; align-items: center; gap: 16px;
  }
  .brand-dot {
    width: 44px; height: 44px; border-radius: 50%;
    background: var(--accent-blue); flex: none;
  }
  .brand-name {
    font-family: "Questrial", sans-serif; font-size: 22px;
    letter-spacing: 1px; color: var(--text-mid); line-height: 1.1;
  }
  .brand-tagline {
    font-family: "Questrial", sans-serif; font-size: 11px;
    letter-spacing: 2px; color: var(--text-mid);
    border-top: 1px solid var(--text-dim); padding-top: 5px; margin-top: 6px;
  }
  .back-divider {
    position: absolute; left: 360px; top: 70px; width: 2px; height: 260px;
    background: var(--accent-teal);
  }
  .contact { position: absolute; left: 390px; top: 68px; color: var(--text-light); }
  .contact-name {
    font-family: "Michroma", sans-serif; font-size: 22px;
    letter-spacing: 4px; color: var(--accent-teal);
  }
  .contact-title {
    font-family: "Michroma", sans-serif; font-size: 11px;
    letter-spacing: 3px; color: var(--text-mid); margin-bottom: 18px;
  }
  .contact-line {
    display: flex; align-items: center; gap: 12px;
    font-family: "Roboto", sans-serif; font-size: 19px; line-height: 30px;
  }
  .contact-line svg { width: 18px; height: 18px; flex: none; }
  .contact-line .spacer { width: 18px; flex: none; }
  .contact-licenses {
    font-family: "Roboto", sans-serif; font-size: 19px; margin-top: 14px;
  }

  /* Front side — brushed metal */
  .card--front {
    top: 447px;
    background:
      repeating-linear-gradient(90deg, rgba(255,255,255,0.05) 0 1px, rgba(0,0,0,0.04) 1px 3px, rgba(255,255,255,0) 3px 5px),
      linear-gradient(120deg, var(--metal-dark), var(--metal-light) 45%, var(--metal-mid) 75%, var(--metal-dark));
    border: 6px solid #c8c8c8;
    box-shadow: inset 0 0 0 2px #9a9a9a;
  }
  .front-lockup {
    position: absolute; left: 62px; top: 120px;
    display: flex; align-items: center;
  }
  .front-dot {
    width: 120px; height: 120px; border-radius: 50%;
    background: var(--metal-ink); flex: none;
    box-shadow: 1px 1px 2px rgba(0,0,0,0.35);
  }
  .front-divider {
    width: 2px; height: 150px; background: var(--metal-ink);
    margin: 0 26px; box-shadow: 1px 0 1px rgba(0,0,0,0.25);
  }
  .front-name {
    font-family: "Questrial", sans-serif; font-size: 34px;
    letter-spacing: 1.5px; color: var(--metal-ink);
    text-shadow: 1px 1px 1px rgba(0,0,0,0.35);
  }
  .front-rule { height: 2px; background: var(--metal-line); margin: 10px 0 8px; }
  .front-tagline {
    font-family: "Questrial", sans-serif; font-size: 19px;
    letter-spacing: 3px; color: var(--metal-ink);
    text-shadow: 1px 1px 1px rgba(0,0,0,0.35);
  }
</style>
</head>
<body>
<main class="sheet">

  <section class="card card--back" aria-label="Card back with contact details">
    <div class="brand">
      <span class="brand-dot"></span>
      <div>
        <div class="brand-name">TORVALE HOLDINGS, LLC</div>
        <div class="brand-tagline">COMMERCIAL &amp; RESIDENTIAL</div>
      </div>
    </div>
    <div class="back-divider"></div>
    <div class="contact">
      <div class="contact-name">LEM KORRIN</div>
      <div class="contact-title">MANAGING BROKER</div>
      <div class="contact-line">
        <svg viewBox="0 0 24 24" aria-hidden="true"><path fill="#959595" d="M3 8c0-2 2-3 9-3s9 1 9 3v2h-5V8H8v2H3zM6 11h12l2 8H4zm6 2a2.5 2.5 0 100 5 2.5 2.5 0 000-5z"/></svg>
        <span>555.261.9047</span>
      </div>
      <div class="contact-line"><span class="spacer"></span><span>555-730-4158</span></div>
      <div class="contact-line">
        <svg viewBox="0 0 24 24" aria-hidden="true"><rect x="2" y="5" width="20" height="14" rx="2" fill="#959595"/><path d="M3 6l9 7 9-7" fill="none" stroke="#232323" stroke-width="1.6"/></svg>
        <span>info@torvaleholdings.example</span>
      </div>
      <div class="contact-licenses">BRE: 07261843 NMLS: 6827354</div>
    </div>
  </section>

  <section class="card card--front" aria-label="Card front, brushed metal">
    <div class="front-lockup">
      <span class="front-dot"></span>
      <span class="front-divider"></span>
      <div>
        <div class="front-name">TORVALE HOLDINGS, LLC</div>
        <div class="front-rule"></div>
        <div class="front-tagline">COMMERCIAL &amp; RESIDENTIAL</div>
      </div>
    </div>
  </section>

</main>
</body>
</html>
```